Business cards for Remote DBA team

Business cards for team offering database administration, consultation, machine learning and AI services. As of now team is using both
www.korvilnet.cz and www.brestmoorlab.cz URLs

Target Market(s)

IT managers

Industry/Entity Type

It Professional

Contact Information for Business Card

Should include logo
name, email, phone, twitter tag

Font styles to use
Sans Serif

Colors

Designer to choose colors to be used in the design.

```html
<!DOCTYPE html>
<html lang="en">
<head>
<meta charset="utf-8">
<title>Brestmoor Lab – Business Cards</title>
<link href="https://fonts.googleapis.com/css2?family=Lato:wght@400;700;900&display=swap" rel="stylesheet">
<style>
  :root {
    --backdrop: #8b4a22;
    --card-blue: #138dc5;
    --card-white: #ffffff;
    --ink-white: #ffffff;
    --brand-blue: #1a8ac4;
    --card-shadow: rgba(0, 0, 0, 0.45);
  }
  html, body {
    margin: 0;
    padding: 0;
    overflow: hidden;
  }
  body {
    width: 1200px;
    height: 900px;
    background: var(--backdrop);
    position: relative;
    font-family: "Lato", Arial, sans-serif;
  }
  .card {
    position: absolute;
    left: 330px;
    width: 556px;
    height: 344px;
    box-shadow: 3px 4px 5px var(--card-shadow);
    box-sizing: border-box;
  }
  .card--front {
    top: 90px;
    background: var(--card-blue);
    color: var(--ink-white);
    text-align: center;
  }
  .card--back {
    top: 469px;
    width: 559px;
    background: var(--card-white);
  }
  .contact {
    position: absolute;
    left: 0;
    right: 0;
    top: 106px;
  }
  .contact__name {
    margin: 0;
    font-weight: 700;
    font-size: 20px;
    letter-spacing: 0.2px;
    line-height: 26px;
  }
  .contact__rule {
    width: 132px;
    height: 1px;
    margin: 10px auto 10px;
    background: var(--ink-white);
  }
  .contact__line {
    margin: 0;
    font-size: 16.5px;
    line-height: 21px;
  }
  .contact__divider {
    display: flex;
    align-items: center;
    justify-content: center;
    gap: 4px;
    margin: 6px 0 3px;
  }
  .contact__divider-line {
    width: 52px;
    height: 1px;
    background: var(--ink-white);
  }
  .contact__dot {
    width: 18px;
    height: 18px;
    border-radius: 50%;
    background: var(--ink-white);
  }
  .brand {
    position: absolute;
    left: 0;
    right: 0;
    top: 172px;
    display: flex;
    align-items: center;
    justify-content: center;
    gap: 14px;
  }
  .brand__dot {
    width: 34px;
    height: 34px;
    border-radius: 50%;
    background: var(--brand-blue);
  }
  .brand__name {
    font-weight: 900;
    font-size: 38px;
    color: var(--brand-blue);
    letter-spacing: 0.5px;
    text-transform: uppercase;
  }
</style>
</head>
<body>
  <section class="card card--front" aria-label="Business card front">
    <div class="contact">
      <h1 class="contact__name">MILAN DVORSKY</h1>
      <div class="contact__rule"></div>
      <p class="contact__line">042-918 305 664</p>
      <p class="contact__line">hello@brestmoorlab.cz</p>
      <div class="contact__divider">
        <span class="contact__divider-line"></span>
        <span class="contact__dot"></span>
        <span class="contact__divider-line"></span>
      </div>
      <p class="contact__line">chatterloop.cz/brestmoorlab</p>
    </div>
  </section>

  <section class="card card--back" aria-label="Business card back">
    <div class="brand">
      <span class="brand__dot"></span>
      <span class="brand__name">Brestmoor Lab</span>
    </div>
  </section>
</body>
</html>
```